Construction Company Needs Letterhead Design

We recently had a new logo designed and would like to have our letterhead updated to a trendier design. We are a concrete construction company based out of Iowa, but do work for Agricultural businesses across the Midwest.

Industry/Entity Type

Construction

Colors
ec1f27
000000
ffffff

Requirements
Must have
• Must stay within our current color scheme of red/black/white. Must have have our address, phone number, e-mail address, etc. printed on the letterhead as well.

```html
<!DOCTYPE html>
<html lang="en">
<head>
<meta charset="utf-8">
<title>Harrowfield Letterhead</title>
<link rel="stylesheet" href="https://fonts.googleapis.com/css2?family=Open+Sans:wght@400;600;700;800&family=Roboto+Condensed:wght@400;700&display=swap">
<style>
  :root {
    --brand-red: #ec1f27;
    --ink: #000000;
    --paper: #ffffff;
    --text-grey: #666666;
    --dark-grey: #333333;
    --backdrop: #d1d2d4;
  }
  * { box-sizing: border-box; margin: 0; padding: 0; }
  html, body { width: 1200px; height: 1200px; overflow: hidden; }
  body {
    background: var(--backdrop);
    font-family: "Open Sans", sans-serif;
    position: relative;
  }
  .letterhead {
    position: absolute;
    left: 279px; top: 111px;
    width: 642px; height: 907px;
    background: var(--paper);
  }
  .abs { position: absolute; }

  .brand {
    left: 53px; top: 79px;
    display: flex; align-items: center; gap: 8px;
  }
  .brand-mark { width: 32px; height: 32px; background: var(--brand-red); }
  .brand-name {
    font-family: "Open Sans", sans-serif;
    font-weight: 800; font-size: 21px; letter-spacing: 0.5px;
    color: var(--ink); line-height: 1;
  }

  .address {
    right: 50px; top: 83px;
    font-size: 11px; color: var(--dark-grey);
  }
  .header-rule {
    left: 278px; top: 100px; width: 314px; height: 2px; background: var(--ink);
  }
  .contact-line {
    right: 50px; display: flex; align-items: center; gap: 5px;
    font-size: 7.5px; color: var(--dark-grey);
  }
  .contact-line svg { width: 8px; height: 8px; fill: var(--brand-red); }
  .phone { top: 110px; }
  .fax { top: 126px; }

  .recipient { left: 51px; top: 224px; color: var(--dark-grey); }
  .recipient .salutation { font-size: 11px; font-weight: 700; }
  .recipient .salutation span {
    display: inline-block; width: 62px; border-bottom: 1px solid var(--dark-grey);
  }
  .recipient .designation { font-size: 7px; margin-top: 1px; }
  .recipient .company { font-size: 7.5px; font-weight: 700; margin-top: 2px; }
  .date {
    right: 53px; top: 224px;
    font-size: 11px; font-weight: 700; color: var(--dark-grey);
  }

  .body-copy { left: 51px; top: 303px; width: 540px; }
  .body-copy p {
    font-family: "Roboto Condensed", sans-serif;
    font-size: 11.2px; line-height: 12.9px; color: var(--text-grey);
    text-align: justify; margin-bottom: 13.5px;
  }

  .signature {
    left: 51px; top: 699px; width: 96px; height: 26px;
    background: linear-gradient(90deg, #f1f1f1, #fafafa);
    border-bottom: 1px solid var(--dark-grey);
  }
  .signer { left: 52px; top: 738px; }
  .signer .name {
    font-size: 13.5px; font-weight: 700; color: var(--brand-red); letter-spacing: 0.3px;
  }
  .signer .role { font-size: 10px; color: var(--dark-grey); margin-top: 1px; }

  .footer-rule {
    left: 51px; top: 847px; width: 483px; height: 2px; background: var(--ink);
  }
  .footer-contact {
    left: 51px; display: flex; align-items: center; gap: 10px;
    font-size: 7px; color: var(--dark-grey);
  }
  .footer-contact svg { width: 11px; height: 10px; }
  .email { top: 832px; }
  .web { top: 854px; }
  .footer-brand {
    left: 549px; top: 826px; width: 38px; height: 38px;
    display: flex; flex-direction: column; align-items: center; gap: 3px;
  }
  .footer-brand .brand-mark { width: 22px; height: 22px; }
  .footer-brand .brand-name { font-size: 5.5px; letter-spacing: 0; }
</style>
</head>
<body>
  <main class="letterhead">
    <header>
      <div class="abs brand">
        <div class="brand-mark"></div>
        <div class="brand-name">HARROWFIELD</div>
      </div>
      <div class="abs address">27 Prairie Mill Rd. Ames, IA 50010</div>
      <div class="abs header-rule"></div>
      <div class="abs contact-line phone">
        <svg viewBox="0 0 10 10"><path d="M2 0.5 L3.6 2.6 L2.8 3.6 Q4 6 6.4 7.2 L7.4 6.4 L9.5 8 L8.4 9.5 Q1.5 8 0.5 1.6 Z"/></svg>
        +123-555-0199
      </div>
      <div class="abs contact-line fax">
        <svg viewBox="0 0 10 10"><rect x="2.5" y="0.5" width="5" height="3"/><rect x="0.5" y="3.5" width="9" height="4" rx="1"/><rect x="2.5" y="6.5" width="5" height="3" fill="#fff" stroke="#ec1f27" stroke-width="0.8"/></svg>
        +123-555-0199
      </div>
    </header>

    <section class="abs recipient">
      <div class="salutation">Dear, Mr<span>&nbsp;</span></div>
      <div class="designation">Designation</div>
      <div class="company">COMPANY NAME</div>
    </section>
    <div class="abs date">DATE:08/02/2018</div>

    <section class="abs body-copy">
      <p>Lorem Ipsum is simply dummy text of the printing and typesetting industry. Lorem Ipsum has been the industry's standard dummy text ever since the1500s,when an unknown printer took a galley of type and scrambled it to make a type specimen book. It has survived not only five centuries, but also the leap into electronic typesetting, remaining essentially unchanged. It was popularised in the 1960s with the release of Typeline sheets containing Lorem Ipsum passages,and more recently with desktop publishing software like Folio PageCraft including versions of Lorem Ipsum.</p>
      <p>Lorem Ipsum is simply dummy text of the printing and typesetting industry. Lorem Ipsum has been the industry's standard dummy text ever since the1500s,when an unknown printer took a galley of type and scrambled it to make a type specimen book. It has survived not only five centuries, but also the leap into electronic typesetting, remaining essentially unchanged. It was popularised in the 1960s with the release of Typeline sheets containing Lorem Ipsum passages,and more recently with desktop publishing software like Folio PageCraft including versions of Lorem Ipsum.</p>
      <p>Lorem Ipsum is simply dummy text of the printing and typesetting industry. Lorem Ipsum has been the industry's standard dummy text ever since the1500s,when an unknown printer took a galley of type and scrambled it to make a type specimen book. It has survived not only five centuries, but also the leap into electronic typesetting, remaining essentially unchanged. It was popularised in the 1960s with the release of Typeline sheets containing Lorem Ipsum passages,and more recently with desktop publishing software like Folio PageCraft including versions of Lorem Ipsum.</p>
      <p>Lorem Ipsum is simply dummy text of the printing and typesetting industry. Lorem Ipsum has been the industry's standard dummy text ever since the1500s,when an unknown printer took a galley of type and scrambled it to make a type specimen book. It has survived not only five centuries, but also the leap into electronic typesetting, remaining essentially unchanged. It was popularised in the 1960s with the release of Typeline sheets containing Lorem Ipsum passages,and more recently with desktop publishing software like Folio PageCraft including versions of Lorem Ipsum.</p>
    </section>

    <div class="abs signature" role="img" aria-label="Handwritten signature"></div>
    <section class="abs signer">
      <div class="name">YOUR NAME</div>
      <div class="role">Designation</div>
    </section>

    <footer>
      <div class="abs footer-contact email">
        <svg viewBox="0 0 11 10"><rect x="0.5" y="1" width="10" height="8" fill="#ec1f27"/><path d="M0.5 1 L5.5 5.5 L10.5 1 M0.5 9 L4 5 M10.5 9 L7 5" stroke="#fff" stroke-width="0.9" fill="none"/></svg>
        info@harrowfield.com
      </div>
      <div class="abs footer-rule"></div>
      <div class="abs footer-contact web">
        <svg viewBox="0 0 10 10"><g fill="none" stroke="#ec1f27" stroke-width="0.9"><circle cx="5" cy="5" r="4.4"/><ellipse cx="5" cy="5" rx="2" ry="4.4"/><path d="M0.6 5 H9.4 M1.4 2.7 H8.6 M1.4 7.3 H8.6"/></g></svg>
        www.harrowfield.com
      </div>
      <div class="abs footer-brand">
        <div class="brand-mark"></div>
        <div class="brand-name">HARROWFIELD</div>
      </div>
    </footer>
  </main>
</body>
</html>
```